New web design for a service provider in the medical field

We are looking for a new design for our website. We are a company that repairs and sells medical endoscopes. Our customers include doctors and hospitals. Our current website can be found at https://lumenfix.example/en/lumenfix-english.
We need a new web design (without programming) for the following 3 pages:
-Startpage https://lumenfix.example/en/lumenfix-english/
-Used endoscopes https://lumenfix.example/en/used-endoscopes/
-Purchase https://lumenfix.example/en/purchase/
The design should be modern and stylish.
The blue color of the logo should be reflected on the page, but not too intrusive.
I have uploaded the images from the header. If more images are needed, let me know and I will upload them.

Target Market(s)
Doctors and hospitals

```html
<!DOCTYPE html>
<html lang="en">
<head>
<meta charset="utf-8">
<title>lumenFIX – Endoscope repair and used endoscopes</title>
<link rel="stylesheet" href="https://fonts.googleapis.com/css2?family=Montserrat:wght@400;500;600&family=Roboto:wght@400;500;700&display=swap">
<style>
:root{
  --blue:#0a74bf;
  --blue-deep:#0d56ad;
  --navy:#0e2a44;
  --ink:#1e2328;
  --grey:#5c6670;
  --pale:#e6eef7;
  --white:#fff;
}
*{box-sizing:border-box;margin:0;padding:0}
html,body{width:1200px;height:3337px;overflow:hidden}
body{font-family:"Roboto",sans-serif;color:var(--ink);background:var(--white);position:relative}
.abs{position:absolute}
.btn{display:inline-flex;align-items:center;justify-content:center;height:34px;padding:0 30px;border-radius:17px;font:500 14px "Roboto",sans-serif;color:var(--white);background:var(--blue);text-transform:uppercase;text-decoration:none;box-shadow:0 8px 14px rgba(10,116,191,.35);white-space:nowrap}
.btn.dark{background:var(--navy);box-shadow:none}
.brand{font:600 22px "Montserrat",sans-serif;color:var(--navy)}

/* header */
.header{top:0;left:0;width:1200px;height:128px;background:#f4f7fb}
.header .brand{left:122px;top:48px}
.contact-bar{right:110px;top:20px;display:flex;align-items:center;gap:14px;font:400 14px "Roboto",sans-serif;color:var(--ink)}
.contact-bar svg{vertical-align:-2px;margin-right:6px}
.lang{background:var(--navy);color:var(--white);border-radius:18px;height:36px;width:145px;display:flex;align-items:center;justify-content:space-between;padding:0 22px;font-weight:500;font-size:14px}
.top-menu{right:110px;top:83px;display:flex;gap:65px;font:500 14px "Roboto",sans-serif;color:var(--ink)}
.main-nav{top:128px;left:0;width:1200px;height:52px;background:var(--blue-deep);display:flex;align-items:center;justify-content:center;gap:50px;font:500 14.5px "Roboto",sans-serif;color:var(--white)}
.main-nav span svg{margin-left:8px}

/* hero */
.hero{top:180px;left:0;width:1200px;height:951px;background:linear-gradient(135deg,#e4edf6,#dfe9f3 60%,#e8eff7)}
.hero .eyebrow{left:110px;top:95px;font:600 27px "Montserrat",sans-serif}
.hero h1{left:110px;top:138px;font:700 38px/57px "Roboto",sans-serif;text-transform:uppercase}
.hero .lead{left:110px;top:255px;width:460px;font:400 15px/27px "Montserrat",sans-serif;color:var(--grey)}
.hero .btn{left:111px;top:322px}
.circle{border-radius:50%;background:var(--blue)}
.arch{border-radius:180px 180px 0 0}
.hero-img{left:709px;top:36px;width:362px;height:439px;background:linear-gradient(160deg,#c9dde9,#a9c6cf 50%,#d7e4e6)}
.cards{top:503px;left:113px;display:flex;gap:15px}
.card{width:315px;height:359px;background:var(--white);border-radius:6px;position:relative;text-align:center}
.card.repair{background:var(--blue-deep);color:var(--white);padding-top:34px}
.card.repair h3{font:400 30px/34px "Roboto",sans-serif}
.card.repair h4{font:500 20px/24px "Roboto",sans-serif;margin-top:14px}
.card.repair hr{width:84px;border:0;border-top:2px solid var(--white);margin:12px auto 11px}
.card.repair p{font:400 15px/26.5px "Montserrat",sans-serif;padding:0 18px}
.card.repair .btn{position:absolute;left:68px;bottom:-18px}
.card .photo{margin:7px;height:172px}
.card h3.title{font:400 30px "Roboto",sans-serif;margin-top:16px}
.card h4.sub{font:400 21px "Roboto",sans-serif;margin-top:20px}
.card .btn{margin-top:14px}

/* intro */
.intro{top:1131px;left:0;width:1200px;height:444px;text-align:center}
.intro h2{margin-top:78px;font:600 27px/36px "Montserrat",sans-serif}
.intro h2 em{font-style:normal;color:var(--blue)}
.intro .big{font:500 42px "Roboto",sans-serif;color:#555c63;margin-top:4px}
.intro p{width:660px;margin:14px auto 0;font:400 16px/27px "Montserrat",sans-serif;color:var(--grey)}
.brands{display:flex;justify-content:center;gap:22px;margin-top:22px}
.brands .btn{width:145px;padding:0}

/* values */
.values{top:1575px;left:0;width:1200px;height:601px;background:linear-gradient(120deg,#e3ebf4,#dbe6f1 50%,#e6edf5)}
.values h2{width:100%;top:70px;text-align:center;font:600 26px "Montserrat",sans-serif}
.values h2 em{font-style:normal;color:var(--blue)}
.feat{width:392px;height:76px;border-left:5px solid var(--blue-deep);padding:6px 0 0 20px}
.feat h5{font:500 17px "Montserrat",sans-serif;color:#444c54;text-transform:uppercase}
.feat p{font:400 16px/23px "Montserrat",sans-serif;color:var(--ink);margin-top:6px;width:340px}
.feat.active{background:var(--blue);color:var(--white);height:98px;padding-top:12px}
.feat.active h5,.feat.active p{color:var(--white)}
.values .btn{left:434px;top:489px;width:334px;padding:0}

/* call */
.call{top:2176px;left:0;width:1200px;height:614px}
.call-img{left:109px;top:85px;width:360px;height:439px;background:linear-gradient(170deg,#d8d4cf,#a9937f 55%,#e7e6ea)}
.call .eyebrow{left:613px;top:175px;font:600 27px "Montserrat",sans-serif}
.call h2{left:613px;top:220px;font:700 38px "Roboto",sans-serif}
.call p{left:613px;top:285px;font:400 21px/45px "Montserrat",sans-serif;color:var(--grey)}
.call .btn{left:614px;top:394px}

/* footer */
.footer{top:2790px;left:0;width:1200px;height:547px;background:var(--blue-deep);color:var(--white)}
.footer .brand{left:129px;top:94px;color:#3aa7ee;font-size:28px}
.social{right:112px;top:104px;display:flex;gap:18px}
.social i{width:18px;height:18px;border-radius:50%;background:var(--white);display:block}
.footer .rule{left:111px;width:978px;border-top:1px solid rgba(255,255,255,.5)}
.col-div{top:191px;height:293px;border-left:1px solid rgba(255,255,255,.5)}
.footer h6{font:700 16px "Roboto",sans-serif}
.footer .small{font:400 13px/27px "Roboto",sans-serif}
.fcol{top:262px}
.quick li{list-style:none;font:400 13px/27px "Roboto",sans-serif;display:flex;align-items:center;gap:5px}
.quick li::before{content:"";width:11px;height:11px;border:1px solid rgba(255,255,255,.6);border-radius:50%}
.subscribe{width:262px;height:52px;margin-top:12px;border:1px solid rgba(255,255,255,.7);border-radius:3px;display:flex}
.subscribe span{flex:1;padding:0 26px;display:flex;align-items:center;font-size:12px;color:rgba(255,255,255,.8)}
.subscribe b{width:66px;background:var(--navy);display:flex;align-items:center;justify-content:center}
.copy{top:3306px;width:1200px;text-align:center;font:400 12px "Roboto",sans-serif;color:rgba(255,255,255,.8)}
</style>
</head>
<body>

<header class="header abs">
  <div class="brand abs">lumenFIX</div>
  <div class="contact-bar abs">
    <span><svg width="14" height="14" viewBox="0 0 24 24"><path fill="#0d56ad" d="M6.6 10.8a15 15 0 006.6 6.6l2.2-2.2a1 1 0 011-.25 11 11 0 003.6.6 1 1 0 011 1V20a1 1 0 01-1 1A17 17 0 013 4a1 1 0 011-1h3.5a1 1 0 011 1c0 1.25.2 2.45.6 3.6a1 1 0 01-.25 1z"/></svg>- +49 4100 555 010-0</span>
    <span>|</span>
    <span><svg width="15" height="12" viewBox="0 0 24 18"><rect width="24" height="18" rx="2" fill="#0d56ad"/><path d="M1 2l11 8 11-8" stroke="#fff" stroke-width="2" fill="none"/></svg>- info@lumenfix.example</span>
    <span class="lang">ENGLISH <svg width="10" height="7" viewBox="0 0 10 7"><path d="M1 1l4 4 4-4" stroke="#fff" stroke-width="2" fill="none"/></svg></span>
  </div>
  <nav class="top-menu abs"><span>HOME</span><span>PICK-UP ORDER</span><span>ABOUT US</span><span>CONTACT US</span></nav>
</header>

<nav class="main-nav abs">
  <span>ENDOSCOPE REPAIR</span>
  <span>USED ENDOSCOPES<svg width="10" height="7" viewBox="0 0 10 7"><path d="M1 1l4 4 4-4" stroke="#fff" stroke-width="2" fill="none"/></svg></span>
  <span>ENDOSCOPY SYSTEMS</span>
  <span>ENDOSCOPY ACCESSORIES<svg width="10" height="7" viewBox="0 0 10 7"><path d="M1 1l4 4 4-4" stroke="#fff" stroke-width="2" fill="none"/></svg></span>
  <span>PURCHASE</span>
</nav>

<section class="hero abs">
  <div class="eyebrow abs">lumenFIX</div>
  <h1 class="abs">Put your endoscope<br>in reliable hands!</h1>
  <p class="lead abs">We provide high and consistent quality by monitoring all processes. Convince yourself!</p>
  <a class="btn abs">Repair request</a>
  <div class="circle abs" style="left:998px;top:42px;width:145px;height:145px"></div>
  <div class="circle abs" style="left:660px;top:378px;width:98px;height:98px"></div>
  <div class="hero-img arch abs" role="img" aria-label="Close-up photo of an endoscope video connector on a pale surface"></div>

  <div class="cards abs">
    <div class="card repair">
      <h3>Repair</h3>
      <h4>Endoscope repair service</h4>
      <hr>
      <p>Manufacturer-independent we repair and maintain endo-scopes, individual components (e.g. processors or light sources), accessories and peripherals of the manufacturers Orvex, Pantra and Fujora.</p>
      <a class="btn">Repair request</a>
    </div>
    <div class="card">
      <div class="photo" role="img" aria-label="Photo of a business handshake with a doctor holding a blue clipboard" style="background:linear-gradient(120deg,#2c3a52,#7b9bc0 45%,#e8edf3 70%,#2a63c8)"></div>
      <h3 class="title">Sale</h3>
      <h4 class="sub">Used endoscopes</h4>
      <a class="btn dark">Purchase request</a>
    </div>
    <div class="card">
      <div class="photo" role="img" aria-label="Photo of a hand on a laptop keyboard with floating shopping cart icons" style="background:linear-gradient(120deg,#7a8a96,#b9c4cc 50%,#d9c2b3 75%,#8d9aa2)"></div>
      <h3 class="title">Purchase</h3>
      <h4 class="sub">Used endoscopes</h4>
      <a class="btn dark">Sell device</a>
    </div>
  </div>
</section>

<section class="intro abs">
  <h2>Endoscope repairs and second hand<br>endoscopes from <em>lumenFIX</em></h2>
  <div class="big">– cause the outcome matters!</div>
  <p>lumenFIX is a privileged partner for the start-up facility or optimisation of existing healthcare facilities, doctor’s offices and hospitals. The quality and reliability of our products and our offered service are our best advertisement!</p>
  <div class="brands"><a class="btn dark">Orvex</a><a class="btn">Pantra</a><a class="btn dark">Fujora</a></div>
</section>

<section class="values abs">
  <h2 class="abs">CAUSE THE <em>OUTCOME MATTERS!</em></h2>
  <div class="feat abs" style="left:174px;top:152px"><h5>One company for everyone</h5><p>We are a service provider for doctors and hospitals!</p></div>
  <div class="feat abs" style="left:676px;top:152px"><h5>Experience characterises us</h5><p>Our team has many years of experience in the business field!</p></div>
  <div class="feat abs" style="left:174px;top:262px"><h5>The product is close to our hearts</h5><p>We repair and sell second hand, flexible endoscopes!</p></div>
  <div class="feat active abs" style="left:676px;top:252px"><h5>Guaranteed service</h5><p>You receive a six-month warranty on all repairs!</p></div>
  <div class="feat abs" style="left:174px;top:372px"><h5>Quality not quantity</h5><p>Reliability and durability instead of inferior replacements!</p></div>
  <div class="feat abs" style="left:676px;top:372px"><h5>Services for everyone</h5><p>Our service includes the manufacturers Orvex, Pantra and Fujora!</p></div>
  <a class="btn abs">Learn more about lumenFIX!</a>
</section>

<section class="call abs">
  <div class="circle abs" style="left:405px;top:90px;width:135px;height:135px"></div>
  <div class="circle abs" style="left:59px;top:426px;width:96px;height:96px"></div>
  <div class="call-img arch abs" role="img" aria-label="Photo of a smiling receptionist on the telephone"></div>
  <div class="eyebrow abs">lumenFIX</div>
  <h2 class="abs">FAULTY ENDOSCOPE?</h2>
  <p class="abs">We ensure quick and smooth repairs!<br>Simple place a</p>
  <a class="btn abs">Pick-up order</a>
</section>

<footer class="footer abs">
  <div class="brand abs">lumenFIX</div>
  <div class="social abs"><i></i><i></i><i></i><i></i><i></i></div>
  <div class="rule abs" style="top:191px"></div>
  <div class="col-div abs" style="left:496px"></div>
  <div class="col-div abs" style="left:801px"></div>
  <div class="fcol abs" style="left:137px">
    <h6>Reach Company Name</h6>
    <div class="small" style="margin-top:12px">Lindenweg 12<br>21400 Musterstadt, Germany</div>
    <div class="small" style="margin-top:29px;padding-left:32px">+49 4100 555 010-0</div>
    <div class="small" style="margin-top:29px;padding-left:32px">info@lumenfix.example</div>
  </div>
  <div class="fcol abs" style="left:522px">
    <h6>Quick Links</h6>
    <ul class="quick" style="margin-top:12px"><li>HOME</li><li>ENDOSCOPE REPAIR</li><li>USED ENDOSCOPES</li><li>ENDOSCOPY SYSTEMS</li><li>ENDOSCOPY ACCESSORIES</li><li>PURCHASE</li></ul>
  </div>
  <div class="fcol abs" style="left:828px">
    <h6>Subscribe</h6>
    <div class="small" style="margin-top:12px">Neque porro quisquam est qui<br>dolorem ipsum quia dolor sit amet,</div>
    <div class="subscribe"><span>Email Address</span><b><svg width="18" height="18" viewBox="0 0 24 24"><path fill="#fff" d="M2 11l20-9-9 20-2-9z"/></svg></b></div>
  </div>
  <div class="rule abs" style="top:484px"></div>
</footer>
<div class="copy abs">lumenFIX © 2022 All Rights Reserved</div>

</body>
</html>
```